Please look at my website to get a better understanding of my business: www.mokeranu.com
This business is about Life Coaching for Families, couples, teenagers and individuals. I work more w parents of teenagers (as well as teenagers) but not so much with young kids.
The card should be fun, not too busy, with a sense of flow and playfulness. Warm colors, artistic style (can have a family sculpture, paining or a picture in it). Basic information about myself and my company

Reason: I extended my due date for next Tuesday, November 13th. Please summit new designs if you haven't done so, and for those who submitted, thank you so much for your time and effort. I will make a decision next Tues, and will contact you if I need to revise some items. Much thanks to you all! Tali

Families, parents, teenagers, couples, individuals.

Business

• Business name: MoKeRaNu! Kinward Circle Life Coaching
My name: Tali Welbrook, CPCC
Description of my work: Tandem-Path life coach
Tel: 555-304-7129
Website: www.MoKeRaNu.com
• Family sculpture, abstract painting or a picture, or simply a nice background w/out a picture added.
• Corporate feeling, cold colors, corporate symbols. no Sunset, or picture of families on the beach.
Don't include bar-code (from uploaded file 1, it is only the designer to find out more about my website).

```html
<!DOCTYPE html>
<html lang="en">
<head>
<meta charset="utf-8">
<title>MoKeRaNu – Kinward Circle Life Coaching</title>
<link rel="stylesheet" href="https://fonts.googleapis.com/css2?family=Source+Sans+3:ital,wght@0,400;1,400&display=swap">
<style>
  :root {
    --page: #ffffff;
    --card-border: #2a2a2a;
    --ink: #111111;
    --ink-soft: #2b2118;
    --brand: #ffffff;
    --wash-cream: #f6dfa6;
    --wash-yellow: #f3e58f;
    --wash-green: #bcc77a;
    --wash-orange: #e8823a;
    --wash-deep: #d9642a;
    --wash-peach: #f1c79a;
  }
  html, body {
    margin: 0;
    width: 1200px;
    height: 764px;
    overflow: hidden;
    background: var(--page);
  }
  .canvas {
    position: relative;
    width: 1200px;
    height: 764px;
    font-family: "Source Sans 3", sans-serif;
  }
  .card {
    position: absolute;
    left: 77px;
    top: 49px;
    width: 1066px;
    height: 642px;
    border: 1px solid var(--card-border);
    overflow: hidden;
  }
  .card__art {
    position: absolute;
    inset: 0;
    background:
      radial-gradient(ellipse 300px 260px at 880px 360px, var(--wash-deep) 0%, rgba(217,100,42,0) 100%),
      radial-gradient(ellipse 220px 180px at 320px 90px, var(--wash-orange) 0%, rgba(232,130,58,0) 100%),
      radial-gradient(ellipse 200px 300px at 120px 300px, var(--wash-green) 0%, rgba(188,199,122,0) 100%),
      radial-gradient(ellipse 360px 300px at 420px 420px, var(--wash-yellow) 0%, rgba(243,229,143,0) 100%),
      linear-gradient(100deg, var(--wash-cream) 0%, var(--wash-yellow) 35%, var(--wash-peach) 60%, var(--wash-orange) 100%);
  }
  .card__headline {
    position: absolute;
    left: 50px;
    top: 110px;
    margin: 0;
    font-style: italic;
    font-weight: 400;
    font-size: 62px;
    line-height: 1;
    color: var(--ink);
    white-space: nowrap;
  }
  .card__brand {
    position: absolute;
    left: 0;
    right: 0;
    top: 250px;
    margin: 0;
    text-align: center;
    font-weight: 400;
    font-size: 120px;
    line-height: 1;
    color: var(--brand);
  }
  .card__person,
  .card__role {
    position: absolute;
    top: 430px;
    margin: 0;
    font-style: italic;
    font-size: 38px;
    line-height: 1;
    color: var(--ink-soft);
    white-space: nowrap;
  }
  .card__person { left: 163px; }
  .card__role { left: 555px; }
  .card__web,
  .card__tel {
    position: absolute;
    top: 572px;
    margin: 0;
    font-size: 34px;
    line-height: 1;
    color: var(--ink);
    white-space: nowrap;
  }
  .card__web { left: 20px; }
  .card__tel { right: 12px; }
</style>
</head>
<body>
  <main class="canvas">
    <section class="card">
      <div class="card__art" role="img" aria-label="Soft abstract painting of warm orange and yellow flowers with green stems"></div>
      <h1 class="card__headline">Kinward Circle Life Coaching</h1>
      <p class="card__brand">MoKeRaNu</p>
      <p class="card__person">Tali Welbrook, CPCC</p>
      <p class="card__role">Tandem-Path life coach</p>
      <p class="card__web">www.MoKeRaNu.com</p>
      <p class="card__tel">Tel: 555-304-7129</p>
    </section>
  </main>
</body>
</html>
```